Banner ads to promote training courses

Project: Online banners and background skin promoting training courses
Objective: Drive users to sign-up page
Summary:
The Pixel Harbour is launching a series of training courses in the UK aimed at people who want to become games journalists.
Design: Please use the colours and logos of The Pixel Harbour. Please avoid use of photography and concentrate on typographical approaches.
Sizes: 728x90, 300x250, 160x600, 1540x981 (with a 1000 width non-visible central area)
Type: Flash banners and flat background skin
Copy (banners):
Flash panels:
1. Learn to make money writing about video games
2. How to interview developers, review games, write news, get access to PRs and mor
3. Get the tricks of the trade from experienced games journalists
On all panels:
• Sponsored by KV
• BOOK NOW TO SAVE 50%
Copy (skins):
Learn to make money writing about video games
Sponsored by KV
BOOK NOW TO SAVE 50%
Taught by experienced games journalists
Click to learn more!
Target Market(s)
Educated 18-24s with a strong interest in video games
Industry/Entity Type
Trade
Look and feel
Each slider illustrates characteristics of the customer's brand and the style your logo design should communicate.

```html
<!DOCTYPE html>
<html lang="en">
<head>
<meta charset="utf-8">
<title>The Pixel Harbour – Training Courses Banner</title>
<link rel="stylesheet" href="https://fonts.googleapis.com/css2?family=Varela+Round&family=Open+Sans:wght@400&family=Lora:ital@0;1&display=swap">
<style>
  :root {
    --bg-dark: #1f1f21;
    --bg-mid: #2e2e31;
    --bg-light: #3c3c40;
    --brand-blue: #2f9ad6;
    --brand-blue-dark: #1f6fa3;
    --headline: #ffffff;
    --tag-face: #5fd0ec;
    --tag-fold: #2fa5c6;
    --tag-text: #ffffff;
  }
  html, body {
    margin: 0;
    padding: 0;
    overflow: hidden;
    background: var(--bg-dark);
  }
  .banner {
    position: relative;
    width: 1200px;
    height: 148px;
    overflow: hidden;
    background: linear-gradient(90deg, var(--bg-light) 0%, var(--bg-mid) 30%, var(--bg-dark) 60%, var(--bg-mid) 100%);
  }
  .banner__texture {
    position: absolute;
    inset: 0;
    background: linear-gradient(180deg, rgba(255,255,255,0.05) 0%, rgba(0,0,0,0.15) 100%);
  }
  .brand {
    position: absolute;
    left: 14px;
    top: 18px;
    width: 230px;
    color: var(--brand-blue);
    font-family: "Varela Round", sans-serif;
  }
  .brand__dot {
    display: block;
    width: 42px;
    height: 42px;
    margin-left: 44px;
    border-radius: 50%;
    background: var(--brand-blue);
  }
  .brand__name {
    margin: 8px 0 0;
    font-size: 27px;
    line-height: 1;
    letter-spacing: -0.3px;
    white-space: nowrap;
  }
  .brand__sponsor {
    margin: 6px 0 0 22px;
    font-size: 18px;
    line-height: 1;
    letter-spacing: 0.5px;
    color: var(--brand-blue);
  }
  .headline {
    position: absolute;
    left: 428px;
    top: 58px;
    margin: 0;
    color: var(--headline);
    font-family: "Open Sans", sans-serif;
    font-weight: 400;
    font-size: 24px;
    line-height: 1;
    white-space: nowrap;
  }
  .offer-tag {
    position: absolute;
    right: 0;
    top: 0;
    width: 215px;
    height: 148px;
  }
  .offer-tag__text {
    position: absolute;
    left: 60px;
    top: 22px;
    width: 120px;
    text-align: center;
    color: var(--tag-text);
    font-family: "Lora", serif;
    transform: rotate(-12deg);
  }
  .offer-tag__save {
    display: block;
    font-style: italic;
    font-size: 25px;
    line-height: 1;
  }
  .offer-tag__amount {
    display: block;
    font-size: 40px;
    line-height: 1.1;
  }
</style>
</head>
<body>
  <div class="banner">
    <div class="banner__texture"></div>

    <div class="brand">
      <span class="brand__dot"></span>
      <p class="brand__name">the pixel harbour</p>
      <p class="brand__sponsor">sponsored by KV</p>
    </div>

    <h1 class="headline">Learn to make money writing</h1>

    <div class="offer-tag">
      <svg width="215" height="148" viewBox="0 0 215 148" aria-hidden="true">
        <polygon points="8,22 175,0 215,0 215,118 55,148" fill="var(--tag-face)"/>
        <polygon points="8,22 55,148 30,112" fill="var(--tag-fold)"/>
      </svg>
      <div class="offer-tag__text">
        <span class="offer-tag__save">save</span>
        <span class="offer-tag__amount">50%</span>
      </div>
    </div>
  </div>
</body>
</html>
```